Sales Flyer Design for Cedarline Fryworks, Inc. this flyer should be bold, fun, attritive, and to the point

Our company is called Cedarline Fryworks, Inc. We collect used cooking for restaurants. We provide container for the customer to poor the frying oil into. We provide monthly rebates for cooking oil collected. We provide grease trap cleaning at charge for size of grease trap or grease interceptor. We need a flyer that is competitive and interesting to the potential customer. We would like it to be flashy and attractive. we would like a slot to leave a business card and a section to write a quote on the flyer. We want information about our company as well as the benefits of using our company. Please visit our website www.cedarlinefryworks.com to learn more about our company and what we do. We are family owned and operated. we have been in business since 1992. we service Oregon and Washington in the US. we provide the best service possible. we pick up quickly and are available for emergency calls.

Target Market(s)

Restaurants, retirement facilities, properties who manage several restaurants, sports arenas, schools, any business that has a kitchen or cooks food.

Industry/Entity Type

recycling of used cooking oils and grease trap materials

Font styles to use
Sans Serif

Colors
0054AA
0677BA
7BADD7
CADEEF
E8F1F8
0094D4
00A9DD
6FCCEA
C7EBF8
E9F6FB
59FF00
82FF00
B8FF75
E3FFCB
F4FFEA
FFF300
FFF600
FEFA6F
FFFEC7
FFFEE8
FFC000
F8CF3A
FAE287
FDF2CF
FEFAEE

Requirements
Must have
• a unique design that seperates uf from our competitors. an easy to understand and not to wordy flyer. we would like some animation such as an emoji with the money tongue hanging out when we mention rebating customers. we wants to express the hassle-free benefits of working with us. we want an emphasis on family owned since 1992
Nice to have
• cood color and balance, happy people shaking hands, images of clean oil collection containers, fancy looking vacuum trucks, overall, an engaging flyer that just doesn't get tossed in the dumpster without looking at it.
Should not have
• long paragraphs. Too much dialogue. No cliches. no boring photos.

```html
<!DOCTYPE html>
<html lang="en">
<head>
<meta charset="utf-8">
<title>Cedarline Fryworks, Inc. – Sales Flyer</title>
<link href="https://fonts.googleapis.com/css2?family=Montserrat:wght@300;500;600;700;800&display=swap" rel="stylesheet">
<style>
  :root{
    --yellow:#FFC000;
    --yellow-soft:#F8CF3A;
    --yellow-pale:#FDF2CF;
    --ink:#23252f;
    --band:#2a2c38;
    --grey:#8e8e8e;
    --white:#ffffff;
    --stage:#ececec;
  }
  *{box-sizing:border-box;margin:0;padding:0}
  html,body{width:1200px;height:1200px;overflow:hidden}
  body{background:var(--stage);font-family:'Montserrat',sans-serif;color:var(--ink);position:relative}
  .page{position:absolute;top:200px;height:803px;background:var(--white);overflow:hidden}
  .page--front{left:20px;width:562px}
  .page--back{left:614px;width:568px}
  .page svg.shapes{position:absolute;inset:0;width:100%;height:100%}
  .txt{position:absolute}

  /* front */
  .brand{left:56px;top:78px;display:flex;align-items:center;gap:10px}
  .brand__dot{width:16px;height:16px;border-radius:50%;background:var(--yellow)}
  .brand__name{font-weight:800;font-size:21px;line-height:1.05;letter-spacing:.5px;color:var(--ink);text-transform:uppercase}
  .hero__kicker{left:108px;top:242px;color:var(--white);font-weight:300;font-size:17px;line-height:22px}
  .hero__title{left:108px;top:264px;color:var(--white);font-weight:800;font-size:26px;line-height:28.5px;letter-spacing:.2px}
  .hero__rule{left:108px;top:407px;width:36px;height:3px;background:var(--white)}

  /* back */
  .offer__title{left:20px;top:58px;font-weight:700;font-size:25px;line-height:28.5px;color:var(--ink)}
  .offer__title span{color:var(--yellow)}
  .offer__sub{left:20px;top:174px;font-weight:600;font-size:14px;line-height:28.5px}
  .offer__body{left:20px;top:232px;width:235px;font-weight:700;font-size:13.6px;line-height:15.6px}
  .offer__body span{display:block;text-align:justify;text-align-last:justify;white-space:nowrap}
  .offer__body span.last{text-align-last:left}
  .offer__rule{left:24px;top:368px;width:40px;height:3px;background:var(--ink)}
  .card-slot__label{left:106px;top:624px;width:351px;text-align:center;font-weight:700;font-size:13.5px;color:var(--ink);letter-spacing:.2px}
</style>
</head>
<body>

<!-- FRONT -->
<section class="page page--front">
  <svg class="shapes" viewBox="0 0 562 803">
    <defs>
      <clipPath id="clipGreyLower"><rect x="0" y="352" width="562" height="451"/></clipPath>
      <linearGradient id="gBottles" x1="0" y1="0" x2="1" y2="1">
        <stop offset="0" stop-color="#9b9b9b"/><stop offset=".35" stop-color="#d9d6cf"/><stop offset=".55" stop-color="#e2ae2c"/><stop offset=".75" stop-color="#c9c4b8"/><stop offset="1" stop-color="#5e5f63"/>
      </linearGradient>
      <linearGradient id="gTruck" x1="0" y1="0" x2="0" y2="1">
        <stop offset="0" stop-color="#5f646c"/><stop offset=".35" stop-color="#a5a9ae"/><stop offset=".55" stop-color="#e8772a"/><stop offset=".7" stop-color="#c4c6c9"/><stop offset="1" stop-color="#5a5c60"/>
      </linearGradient>
      <linearGradient id="gJars" x1="0" y1="0" x2="0" y2="1">
        <stop offset="0" stop-color="#d8d8d8"/><stop offset=".3" stop-color="#3c3c40"/><stop offset=".55" stop-color="#eab02a"/><stop offset="1" stop-color="#b0721a"/>
      </linearGradient>
      <linearGradient id="gMeeting" x1="0" y1="0" x2="1" y2="1">
        <stop offset="0" stop-color="#e9872c"/><stop offset=".35" stop-color="#6f9bd0"/><stop offset=".6" stop-color="#f19a3a"/><stop offset="1" stop-color="#3f6fa8"/>
      </linearGradient>
    </defs>

    <rect x="22" y="47" width="43" height="3" fill="var(--yellow)"/>
    <rect x="243" y="44" width="50" height="3" fill="var(--yellow)"/>

    <path d="M0,542 Q240,430 420,600 Q505,690 545,803 L0,803 Z" fill="var(--yellow-soft)"/>
    <circle cx="184" cy="340" r="200" fill="var(--grey)" fill-opacity=".75" clip-path="url(#clipGreyLower)"/>

    <g role="img" aria-label="Photo: oil bottles moving on a bottling line">
      <circle cx="408" cy="323" r="176" fill="url(#gBottles)"/>
    </g>
    <circle cx="470" cy="166" r="53" fill="var(--white)"/>
    <circle cx="467" cy="157" r="14" fill="none" stroke="var(--yellow)" stroke-width="2"/>

    <circle cx="208" cy="324" r="142" fill="var(--ink)"/>

    <g role="img" aria-label="Photo: oil collection vacuum truck">
      <circle cx="94" cy="650" r="83" fill="url(#gTruck)"/>
    </g>
    <g role="img" aria-label="Photo: gloved hand sorting bottles of cooking oil">
      <circle cx="277" cy="650" r="83" fill="url(#gJars)"/>
    </g>
    <g role="img" aria-label="Photo: business partners shaking hands in a meeting">
      <circle cx="460" cy="650" r="83" fill="url(#gMeeting)"/>
    </g>
  </svg>

  <div class="txt brand">
    <span class="brand__dot"></span>
    <span class="brand__name">Cedarline<br>Fryworks, Inc.</span>
  </div>

  <p class="txt hero__kicker">Recycling since 1992</p>
  <h1 class="txt hero__title">Oil Recycling<br>Company<br>In Oregon<br>And Western<br>Washington</h1>
  <span class="txt hero__rule"></span>
</section>

<!-- BACK -->
<section class="page page--back">
  <svg class="shapes" viewBox="0 0 568 803">
    <defs>
      <radialGradient id="gSplash" cx="50%" cy="50%" r="50%">
        <stop offset="0" stop-color="#f1d67a" stop-opacity=".6"/><stop offset=".6" stop-color="#f8e7ae" stop-opacity=".35"/><stop offset="1" stop-color="#fffde8" stop-opacity="0"/>
      </radialGradient>
      <radialGradient id="gEmoji" cx="40%" cy="35%" r="65%">
        <stop offset="0" stop-color="#ffdc55"/><stop offset=".7" stop-color="#f0b021"/><stop offset="1" stop-color="#c98a10"/>
      </radialGradient>
      <linearGradient id="gNozzle" x1="0" y1="0" x2="1" y2="1">
        <stop offset="0" stop-color="#f4f4f2"/><stop offset=".3" stop-color="#2f8f4a"/><stop offset=".5" stop-color="#9a9a9a"/><stop offset=".7" stop-color="#c98a1e"/><stop offset="1" stop-color="#6b4a12"/>
      </linearGradient>
      <linearGradient id="gDrum" x1="0" y1="0" x2="1" y2="1">
        <stop offset="0" stop-color="#2a7d33"/><stop offset=".3" stop-color="#e6b42a"/><stop offset=".55" stop-color="#7fd04a"/><stop offset="1" stop-color="#2a7d33"/>
      </linearGradient>
      <linearGradient id="gPour" x1="0" y1="0" x2="1" y2="1">
        <stop offset="0" stop-color="#3e3e40"/><stop offset=".45" stop-color="#e2b63a"/><stop offset=".7" stop-color="#d9d4c0"/><stop offset="1" stop-color="#5c5a52"/>
      </linearGradient>
      <linearGradient id="gBarrels" x1="0" y1="0" x2="0" y2="1">
        <stop offset="0" stop-color="#cfd3d6"/><stop offset=".45" stop-color="#e9d21c"/><stop offset=".7" stop-color="#f3e23a"/><stop offset="1" stop-color="#8d8f90"/>
      </linearGradient>
    </defs>

    <g role="img" aria-label="Illustration: golden oil splash in the background">
      <ellipse cx="400" cy="300" rx="240" ry="330" fill="url(#gSplash)"/>
    </g>

    <circle cx="417" cy="220" r="151" fill="var(--yellow-soft)"/>
    <circle cx="415" cy="220" r="95" fill="var(--ink)"/>
    <g role="img" aria-label="Photo: fuel nozzle pouring golden oil">
      <circle cx="415" cy="220" r="86" fill="url(#gNozzle)"/>
    </g>

    <g role="img" aria-label="Emoji: grinning face with money eyes and tongue">
      <circle cx="242" cy="84" r="33" fill="url(#gEmoji)"/>
    </g>

    <rect x="0" y="590" width="568" height="213" fill="var(--band)"/>

    <circle cx="96" cy="442" r="39" fill="var(--yellow-soft)"/>
    <circle cx="283" cy="442" r="39" fill="var(--yellow-soft)"/>
    <circle cx="470" cy="442" r="39" fill="var(--yellow-soft)"/>

    <g role="img" aria-label="Photo: gloved hand opening a clean green oil container">
      <circle cx="96" cy="532" r="89" fill="url(#gDrum)"/>
    </g>
    <g role="img" aria-label="Photo: cooking oil poured from a bottle into a glass">
      <circle cx="283" cy="532" r="89" fill="url(#gPour)"/>
    </g>
    <g role="img" aria-label="Photo: rows of yellow oil barrels in a warehouse">
      <circle cx="470" cy="532" r="89" fill="url(#gBarrels)"/>
    </g>

    <rect x="106" y="609" width="351" height="182" rx="60" fill="var(--yellow-soft)"/>
  </svg>

  <h2 class="txt offer__title">Revolutionize<br>Your Rewards:<br><span>Effortless Rebates,<br>Endless Benefits</span></h2>
  <p class="txt offer__sub">Where Customer Satisfaction<br>Meets Hassle-Free Excellence</p>
  <p class="txt offer__body">
    <span>We recycle used cooking oil</span>
    <span>and convert it into renewable,</span>
    <span>clean-burning biodiesel, as well</span>
    <span>as provide maintenance and</span>
    <span>repair services. Learn more</span>
    <span>about our company and what</span>
    <span class="last">we can do for your business.</span>
  </p>
  <span class="txt offer__rule"></span>

  <p class="txt card-slot__label">PLACE YOUR CARD HERE</p>
</section>

</body>
</html>
```